New emergency medical service needs a marketing flyer for prospective customers

We need a tri fold brochure on an 8.5 X 11 stock for a new emergency medical service in Pennsylvania. We provide basic first aid and now Covid-19 pre screening and temperature monitoring for special events, large gatherings and businesses. Examples of these would be but not limited to: Sporting events, carnivals, festivals, craft shows, warehouses, churches, manufacturing facilities, industrial buildings, large construction sites, multi occupancy officer buildings. The market for this is pretty much untouched and endless. we would like to use gray as the back ground color and obviously our logo. The final design should grab their attention and communicate the importance of having trained and certified professionals at their event or facility. We want to give them that piece of mind they are in good hands with us.

Target Market(s)

primary focus is going to be on businesses with large offices, large buildings or lots of foot traffic in and out of the building

Requirements
Must have
• gray background, pictures, company phone # , company web site, and contact email address. I will provide all that information to the winner to add at the end.
Nice to have
• pictures that covers the whole front cover with logo at top

```html
<!DOCTYPE html>
<html lang="en">
<head>
<meta charset="utf-8">
<title>Medique Medical Services — Tri-fold Brochure</title>
<link rel="stylesheet" href="https://fonts.googleapis.com/css2?family=Libre+Baskerville:wght@400;700&family=Oswald:wght@500&family=Open+Sans:wght@400;600;700&family=Montserrat:wght@400;500&display=swap">
<style>
  :root{
    --stage:#e4e6e9;
    --paper:#e3e4e6;
    --paper-light:#efeff0;
    --blue:#2f6fc2;
    --blue-deep:#1f3fa8;
    --blue-sky:#29b6e8;
    --navy:#1b2d6b;
    --ink:#3f4650;
    --white:#ffffff;
  }
  *{box-sizing:border-box;margin:0;padding:0}
  html,body{width:1200px;height:675px;overflow:hidden;background:var(--stage)}
  body{position:relative;font-family:"Open Sans",sans-serif;color:var(--ink)}
  .spread{position:absolute;top:118px;width:570px;height:440px;display:flex;box-shadow:0 6px 18px rgba(0,0,0,.18)}
  .spread--inside{left:20px}
  .spread--outside{left:610px}
  .panel{position:relative;width:190px;height:100%;overflow:hidden;background:var(--paper)}
  .panel + .panel{border-left:1px solid rgba(0,0,0,.08)}
  .panel svg.deco{position:absolute;left:0;width:190px;pointer-events:none}
  .photo{position:absolute;overflow:hidden}
  .heading{font-family:"Libre Baskerville",serif;font-weight:700;text-transform:uppercase;letter-spacing:.3px}
  .body-copy{font-size:7px;line-height:1.4}

  /* About */
  .panel--about{background:var(--blue);color:var(--white)}
  .panel--about .heading{position:absolute;left:16px;top:110px;font-size:15px}
  .panel--about .copy{position:absolute;left:16px;right:18px;top:136px}
  .panel--about .copy p{margin-bottom:10px}
  .panel--about .photo{left:0;bottom:0;width:190px;height:118px;border-radius:70% 0 0 0/40% 0 0 0;background:linear-gradient(160deg,#b9a98d,#6f7c8c 55%,#3c5472)}

  /* Services */
  .panel--services{background:var(--paper-light)}
  .panel--services .heading{position:absolute;left:18px;top:44px;font-size:13px;color:#2c3340}
  .service{position:absolute;left:18px;display:flex;gap:8px;align-items:center}
  .service__icon{width:22px;height:22px;border-radius:50%;background:var(--blue);flex:none;display:flex;align-items:center;justify-content:center}
  .service__title{font-family:"Oswald",sans-serif;font-size:8px;color:var(--blue-deep);letter-spacing:.2px}
  .service__text{font-size:6.5px;line-height:1.3;width:128px}
  .panel--services .why{position:absolute;left:18px;top:288px;font-size:11.5px;color:var(--blue)}
  .panel--services .why-copy{position:absolute;left:18px;right:14px;top:308px}
  .panel--services .why-copy p{margin-bottom:8px}

  /* Features */
  .panel--features .photo{left:10px;top:-40px;width:210px;height:170px;border-radius:50%;background:linear-gradient(140deg,#c7d2dd,#8fb6c8 45%,#5d6f86)}
  .panel--features .heading{position:absolute;left:16px;top:192px;font-size:11.5px;color:#2c3340}
  .panel--features .intro{position:absolute;left:16px;right:14px;top:212px}
  .panel--features ul{position:absolute;left:16px;right:12px;top:252px;list-style:none}
  .panel--features li{position:relative;padding-left:9px;margin-bottom:9px;font-size:6.5px;line-height:1.35}
  .panel--features li::before{content:"";position:absolute;left:0;top:3px;width:3px;height:3px;border-radius:50%;background:var(--ink)}

  /* Priority */
  .panel--priority .heading{position:absolute;left:18px;top:58px;font-size:12px;color:var(--blue-deep);line-height:1.15}
  .panel--priority .copy{position:absolute;left:18px;right:14px;top:96px}
  .panel--priority .copy p{margin-bottom:8px}
  .panel--priority .photo{left:0;bottom:0;width:190px;height:190px;border-radius:0 90% 0 0/0 30% 0 0;background:linear-gradient(165deg,#d9d4c8,#8b8c88 45%,#3f4246)}

  /* Contact */
  .panel--contact{background:var(--blue);color:var(--white)}
  .contact__badge{position:absolute;left:77px;top:78px;width:36px;height:36px}
  .contact__title{position:absolute;left:0;right:0;top:126px;text-align:center;font-family:"Montserrat",sans-serif;font-size:15px;letter-spacing:1px}
  .contact__list{position:absolute;left:30px;top:162px;list-style:none;font-family:"Montserrat",sans-serif;font-size:8.5px}
  .contact__list li{display:flex;align-items:center;gap:9px;margin-bottom:9px}
  .contact__list svg{width:9px;height:9px;flex:none}
  .contact__quote{position:absolute;left:22px;right:20px;top:272px;text-align:center;font-size:7px;line-height:1.45}

  /* Cover */
  .panel--cover .photo{left:20px;top:24px;width:150px;height:150px;border-radius:50%;background:linear-gradient(135deg,#e7d6b8,#b79b73 40%,#d9a13a 70%,#4a4f5a)}
  .cover__brand{position:absolute;left:0;right:0;top:236px;display:flex;justify-content:center;align-items:center;gap:6px}
  .cover__mark{width:14px;height:14px;border-radius:50%;background:var(--navy)}
  .cover__name{font-family:"Open Sans",sans-serif;font-weight:700;font-size:15px;color:var(--navy);letter-spacing:.5px}
  .cover__sub{position:absolute;left:0;right:0;top:258px;text-align:center;font-weight:700;font-size:8px;color:var(--navy)}
  .cover__tagline{position:absolute;left:20px;right:20px;top:286px;text-align:center;font-weight:600;font-size:8px;line-height:1.35;color:#2c3340}
</style>
</head>
<body>

<section class="spread spread--inside" aria-label="Brochure inside">
  <article class="panel panel--about">
    <svg class="deco" style="top:0" height="110" viewBox="0 0 190 110"><path d="M0 0H190V30C130 30 60 60 0 100Z" fill="#4d8fdc"/><path d="M0 0H190V10C120 12 50 40 0 70Z" fill="#6aa9ea"/></svg>
    <h2 class="heading">About Us</h2>
    <div class="copy body-copy">
      <p>Lorem ipsum dolor sit amet, consectetuer adipiscing elit, sed diam nonummy nibh euismod tincidunt ut laoreet dolore magna aliquam erat volutpat. Ut wisi enim ad minim veniam.</p>
      <p>Lorem ipsum dolor sit amet, consectetuer adipiscing elit, sed diam nonummy nibh euismod tincidunt ut laoreet dolore magna aliquam erat volutpat. Ut wisi enim ad minim veniam.</p>
      <p>Lorem ipsum dolor sit amet, consectetuer adipiscing elit, sed diam nonummy nibh euismod tincidunt.</p>
    </div>
    <div class="photo" role="img" aria-label="Photo of a medic screening construction workers in hard hats"></div>
  </article>

  <article class="panel panel--services">
    <h2 class="heading">Our Services</h2>
    <div class="service" style="top:76px"><span class="service__icon"><svg width="12" height="12" viewBox="0 0 12 12"><path d="M6 10.5 1.5 6A2.5 2.5 0 0 1 6 2.8 2.5 2.5 0 0 1 10.5 6Z" fill="none" stroke="#fff" stroke-width="1.1"/></svg></span><div><div class="service__title">LOREM IPSUM</div><div class="service__text">Lorem ipsum dolor sit amet, consectetuer adipiscing elit.</div></div></div>
    <div class="service" style="top:124px"><span class="service__icon"><svg width="12" height="12" viewBox="0 0 12 12"><rect x="1.5" y="3.5" width="9" height="6.5" rx="1" fill="none" stroke="#fff" stroke-width="1.1"/><path d="M6 5v3.5M4.25 6.75h3.5" stroke="#fff" stroke-width="1.1"/></svg></span><div><div class="service__title">LOREM IPSUM</div><div class="service__text">Lorem ipsum dolor sit amet, consectetuer adipiscing elit.</div></div></div>
    <div class="service" style="top:172px"><span class="service__icon"><svg width="12" height="12" viewBox="0 0 12 12"><path d="M6 10.5 1.5 6A2.5 2.5 0 0 1 6 2.8 2.5 2.5 0 0 1 10.5 6Z" fill="none" stroke="#fff" stroke-width="1.1"/><path d="M3 6.2h1.6l.8-1.3 1 2.4.8-1.1H9" fill="none" stroke="#fff" stroke-width=".8"/></svg></span><div><div class="service__title">LOREM IPSUM</div><div class="service__text">Lorem ipsum dolor sit amet, consectetuer adipiscing elit.</div></div></div>
    <div class="service" style="top:220px"><span class="service__icon"><svg width="12" height="12" viewBox="0 0 12 12"><rect x="3" y="2" width="2.4" height="8" rx="1.2" fill="none" stroke="#fff" stroke-width="1"/><rect x="6.6" y="2" width="2.4" height="8" rx="1.2" fill="none" stroke="#fff" stroke-width="1"/></svg></span><div><div class="service__title">LOREM IPSUM</div><div class="service__text">Lorem ipsum dolor sit amet, consectetuer adipiscing elit.</div></div></div>
    <h3 class="heading why">Why Choose Us:</h3>
    <div class="why-copy body-copy">
      <p>Lorem ipsum dolor sit amet, consectetuer adipiscing elit, sed diam nonummy nibh euismod tincidunt ut laoreet dolore magna aliquam erat volutpat.</p>
      <p>Lorem ipsum dolor sit amet, consectetuer adipiscing elit, sed diam nonummy nibh euismod tincidunt.</p>
    </div>
  </article>

  <article class="panel panel--features">
    <svg class="deco" style="top:0" height="175" viewBox="0 0 190 175"><path d="M0 0H14C-6 60 30 150 130 165 160 168 180 162 190 158V175H0Z" fill="#c9cbcf"/><path d="M0 0H18C2 70 50 140 140 152 165 154 182 150 190 146V160C150 175 40 165 0 80Z" fill="var(--blue-deep)"/></svg>
    <div class="photo" role="img" aria-label="Photo of two medical professionals in masks examining a sample tube in a lab"></div>
    <h2 class="heading">Our Features</h2>
    <p class="intro body-copy">Lorem ipsum dolor sit amet, consectetuer adipiscing elit, sed diam nonummy nibh euismod tincidunt.</p>
    <ul>
      <li>Lorem ipsum dolor sit amet, consectetuer adipiscing elit, sed diam nonummy.</li>
      <li>Lorem ipsum dolor sit amet, consectetuer adipiscing elit, sed diam nonummy.</li>
      <li>Lorem ipsum dolor sit amet, consectetuer adipiscing elit, sed diam nonummy.</li>
    </ul>
    <svg class="deco" style="bottom:0" height="60" viewBox="0 0 190 60"><path d="M20 60C60 20 130 10 190 14V60Z" fill="#c9cbcf"/><path d="M50 60C90 30 150 24 190 28V60Z" fill="var(--blue-deep)"/><path d="M90 60C120 42 160 38 190 42V60Z" fill="var(--blue-sky)"/></svg>
  </article>
</section>

<section class="spread spread--outside" aria-label="Brochure outside">
  <article class="panel panel--priority">
    <svg class="deco" style="top:0" height="60" viewBox="0 0 190 60"><path d="M0 0H190V50C120 50 50 40 0 10Z" fill="var(--blue)"/></svg>
    <h2 class="heading">Your Health<br>Is Our Priority</h2>
    <div class="copy body-copy">
      <p>Lorem ipsum dolor sit amet, consectetuer adipiscing elit, sed diam nonummy nibh euismod tincidunt.</p>
      <p>Trained staff keep every guest safe. We screen, monitor and respond fast so your event or building runs with calm and care from start to finish.</p>
    </div>
    <div class="photo" role="img" aria-label="Photo of masked workers in protective suits in a large open office"></div>
  </article>

  <article class="panel panel--contact">
    <svg class="contact__badge" viewBox="0 0 36 36"><circle cx="18" cy="18" r="15" fill="none" stroke="#fff" stroke-width="1.6" stroke-dasharray="80 14"/><path d="M8 11c2-2 3-2 4 0l1 2c.5 1 0 2-1 2.5 1 2.5 3 4.5 5.5 5.5.5-1 1.5-1.5 2.5-1l2 1c2 1 2 2 0 4-4 2-14-8-14-14Z" fill="#fff"/><text x="22" y="20" font-family="Montserrat,sans-serif" font-size="8" fill="#fff">24</text></svg>
    <h2 class="contact__title">CONTACT US</h2>
    <ul class="contact__list">
      <li><svg viewBox="0 0 10 10"><path d="M5 9.5S1.8 6 1.8 4a3.2 3.2 0 0 1 6.4 0C8.2 6 5 9.5 5 9.5Z" fill="none" stroke="#fff" stroke-width="1"/><circle cx="5" cy="4" r="1" fill="#fff"/></svg>123, lorem country</li>
      <li><svg viewBox="0 0 10 10"><path d="M1.5 2c1-1 1.6-1 2 0l.6 1.2c.3.6 0 1-.5 1.3.6 1.4 1.6 2.4 3 3 .3-.5.7-.8 1.3-.5L9 7.6c1 .5 1 1 0 2C7 10.5 .5 4 1.5 2Z" fill="#fff"/></svg>000 1234 567 89</li>
      <li><svg viewBox="0 0 10 10"><circle cx="5" cy="5" r="4" fill="none" stroke="#fff" stroke-width=".9"/><path d="M1 5h8M5 1c-2 2.5-2 5.5 0 8M5 1c2 2.5 2 5.5 0 8" fill="none" stroke="#fff" stroke-width=".7"/></svg>www.loremipsum.com</li>
      <li><svg viewBox="0 0 10 10"><rect x="1" y="2.5" width="8" height="5.5" fill="none" stroke="#fff" stroke-width=".9"/><path d="M1 2.5 5 6l4-3.5" fill="none" stroke="#fff" stroke-width=".9"/></svg>your@email.com</li>
    </ul>
    <p class="contact__quote">“ Lorem ipsum dolor sit amet, consectetuer adipiscing elit, sed diam nonummy nibh euismod tincidunt ut laoreet dolore magna aliquam erat volutpat. ”</p>
    <svg class="deco" style="bottom:0" height="70" viewBox="0 0 190 70"><path d="M0 30C60 10 140 30 190 60V70H0Z" fill="var(--blue-deep)" opacity=".55"/></svg>
  </article>

  <article class="panel panel--cover">
    <svg class="deco" style="top:0" height="205" viewBox="0 0 190 205"><path d="M0 0H190V40C175 20 160 10 150 6H40C25 12 10 25 0 40Z" fill="var(--blue)"/><path d="M14 120C30 175 110 205 170 160 180 150 186 138 190 128V150C160 205 50 215 10 130Z" fill="var(--blue-deep)"/><path d="M18 130C40 185 120 205 176 158 160 190 60 210 18 130Z" fill="var(--blue-sky)"/><path d="M170 40C188 70 188 100 178 120L190 110V40Z" fill="#c9cbcf"/></svg>
    <div class="photo" role="img" aria-label="Photo of a health worker taking a masked woman's temperature with a forehead thermometer"></div>
    <div class="cover__brand"><span class="cover__mark"></span><span class="cover__name">MEDIQUE</span></div>
    <div class="cover__sub">Medical Services</div>
    <p class="cover__tagline">Provide certified medical professionals for medical standbys at events and businesses.</p>
    <svg class="deco" style="bottom:0" height="60" viewBox="0 0 190 60"><path d="M10 60C50 20 130 10 190 18V60Z" fill="var(--blue-deep)"/><path d="M60 60C100 34 150 30 190 34V60Z" fill="var(--blue-sky)"/></svg>
  </article>
</section>

</body>
</html>
```